Business card design needed

I need a business card for my new Food & Lifestyle Coaching business - "Bloomvale Food & Lifestlye Coaching"

i already have a logo and would like to have that incorporated into the business card, obviously.

i would like a design that says "fresh" and "funky" - my target market is female, aged 20-45 so i want something that will stand out to them when they see it.

My "Company Colour" is Apple Green
Updates

Thankyou to everyone who has submitted a design for my project. At this stage i have quite a large number of designs to chose from and with only a short time until my project closes i am focusing now on chosing from those i have already shortlisted so am unfortunately not considering any new desings.

Thankyou again for your interest in my project.

Target Market(s)

Female, Health Conscious (or looking to improve their health/lifestyle), aged between 20-45

Industry/Entity Type

Business

Contact Information for Business Card

Tamsin Corley
Ph: 0417382946
Email: eatwell@marovex.com

Requirements
Must have
• Must include my existing Logo
Nice to have
• Would be nice to incoirporate and appointment card on the back

```html
<!DOCTYPE html>
<html lang="en">
<head>
<meta charset="utf-8">
<title>Bloomvale Food &amp; Lifestyle Coaching – Business Card</title>
<link rel="stylesheet" href="https://fonts.googleapis.com/css2?family=Source+Sans+3:wght@400;600&family=Alex+Brush&display=swap">
<style>
  :root {
    --apple-green: #84ff00;
    --ribbon-white: #ffffff;
    --page-white: #ffffff;
    --ink-black: #111111;
    --text-white: #ffffff;
  }
  html, body {
    margin: 0;
    padding: 0;
    width: 1200px;
    height: 745px;
    overflow: hidden;
    background: var(--page-white);
  }
  .canvas {
    position: relative;
    width: 1200px;
    height: 745px;
  }
  .card {
    position: absolute;
    left: 53px;
    top: 36px;
    width: 1119px;
    height: 669px;
    background: var(--apple-green);
    overflow: hidden;
  }
  .ribbon-vertical {
    position: absolute;
    left: 187px;
    top: 0;
    width: 37px;
    height: 100%;
    background: var(--ribbon-white);
  }
  .ribbon-horizontal {
    position: absolute;
    left: 0;
    top: 324px;
    width: 100%;
    height: 37px;
    background: var(--ribbon-white);
  }
  .ribbon-knot {
    position: absolute;
    left: 69px;
    top: 200px;
    width: 272px;
    height: 240px;
    background: var(--ribbon-white);
    border-radius: 6px;
  }
  .brand {
    position: absolute;
    right: 67px;
    top: 40px;
    text-align: right;
    color: var(--ink-black);
    font-family: "Source Sans 3", sans-serif;
  }
  .brand-name {
    margin: 0;
    font-size: 150px;
    font-weight: 400;
    line-height: 1;
    letter-spacing: -2px;
  }
  .brand-tagline {
    margin: 22px 0 0;
    font-size: 29px;
    font-weight: 400;
    letter-spacing: -0.3px;
  }
  .person-name {
    position: absolute;
    right: 62px;
    top: 392px;
    margin: 0;
    color: var(--text-white);
    font-family: "Alex Brush", cursive;
    font-size: 82px;
    font-weight: 400;
    line-height: 1;
    letter-spacing: 2px;
  }
  .contact {
    position: absolute;
    right: 44px;
    top: 530px;
    margin: 0;
    text-align: right;
    color: var(--text-white);
    font-family: "Source Sans 3", sans-serif;
    font-size: 38px;
    font-weight: 400;
    line-height: 50px;
    font-style: normal;
  }
</style>
</head>
<body>
<main class="canvas">
  <section class="card" aria-label="Business card front">
    <div class="ribbon-vertical"></div>
    <div class="ribbon-horizontal"></div>
    <div class="ribbon-knot"></div>

    <header class="brand">
      <h1 class="brand-name">Bloomvale</h1>
      <p class="brand-tagline">Food &amp; Lifestyle Coaching</p>
    </header>

    <p class="person-name">Tamsin Corley</p>

    <address class="contact">
      Phone: 0417382946<br>
      eatwell@marovex.com
    </address>
  </section>
</main>
</body>
</html>
```